Redesign Gearcrate.co.uk website for Film,Tv & Photo Industries.

www.gearcrate.co.uk needs a major redesign and new fresh look.
We will be using Quillbrook V1 software and have a company that will do all the coding etc etc.

The website is for people who work in the film, tv and photographic industries and are looking to buy bags and cases for their equipment.
About 14 different Manufacturers will be featured.
Just need a modern home page, everything else will follow this design.
Updates

Hi All, I have altered the description of the project , not that much has altered just giving more info out. regards Rob Calder.

Hi Everyone, I have just uploaded a new logo for the www.gearcrate.co.uk website. regards Rob Calder.

Final logo has been uploaded. Regards Rob.

Reason: Even though there are many good designs a lot of them are the same. I would like to see even more of a modern design even using flat colours that don't follow the colour of the new logo regards Rob.

Having seen many very good designs I would like to see different designs using FLAT colours which are modern . You don't have to stick to the colours of the logo as i can change the red in the logo to match the colour of the website. regards Rob Calder.

Target Market(s)

Artistic People who work in Film , TV and photographic Industries. Photographers, cameramen, Production Companies who need to protect their equipment.
Both Pro and Amateur.

Industry/Entity Type

Software

Requirements
Must have
• open minded
Nice to have
• Modern Look

```html
<!DOCTYPE html>
<html lang="en">
<head>
<meta charset="utf-8">
<title>Gearcrate – Cases for Film, TV &amp; Photo</title>
<link href="https://fonts.googleapis.com/css2?family=Open+Sans:wght@400;600;700&family=Oswald:wght@500;700&display=swap" rel="stylesheet">
<style>
:root{
  --red:#c8141c;
  --red-dark:#8f0a10;
  --ink:#222;
  --dark:#1c1c1c;
  --darker:#111;
  --line:#dcdcdc;
  --panel:#efefef;
  --white:#fff;
  --blue:#1c4fc4;
}
*{margin:0;padding:0;box-sizing:border-box}
html,body{width:1200px;height:2452px;overflow:hidden}
body{font-family:"Open Sans",Arial,sans-serif;color:var(--ink);background:var(--white);font-size:12px;position:relative}
ul{list-style:none}
.wrap{width:860px;margin:0 auto;position:relative}

/* top bar */
.topbar{height:34px;background:var(--dark);color:#ddd}
.topbar .wrap{display:flex;justify-content:flex-end;align-items:center;height:34px;gap:18px;font-size:11px;font-weight:600}
.topbar .reg{color:#ff4b4b}
.topbar .sep{color:#666}
.social{display:flex;gap:8px}
.social span{width:14px;height:14px;border-radius:50%;background:#ccc}

/* header */
.header{height:119px}
.logo{position:absolute;left:0;top:30px;display:flex;align-items:center;gap:10px;font-size:46px;font-weight:700;color:var(--red);letter-spacing:-1px;line-height:1}
.logo i{width:40px;height:40px;background:var(--red);display:block}
.phone{position:absolute;left:448px;top:42px;width:196px;height:36px;border-radius:20px;border:1px solid var(--line);background:#f7f7f7;display:flex;align-items:center;gap:10px;padding-left:10px;font-size:20px;color:#333;white-space:nowrap}
.phone svg{width:20px;height:20px;flex:none}
.cart{position:absolute;left:670px;top:10px;width:178px;height:84px;border:1px solid var(--line);padding:6px 10px;font-size:13px;color:#333;line-height:22px}
.cart b{font-weight:600;display:block;border-bottom:1px solid var(--line)}
.cart svg{position:absolute;right:12px;top:32px;width:46px;height:40px}

/* nav */
.nav{height:40px;background:linear-gradient(var(--red),var(--red-dark))}
.nav .wrap{display:flex;align-items:center;height:40px;gap:34px;color:var(--white);font-size:12px;font-weight:600}
.search{margin-left:auto;width:292px;height:24px;background:var(--white);display:flex;align-items:center;justify-content:space-between;padding-left:8px;color:#999;font-size:11px;font-weight:400}
.search span{width:40px;height:24px;background:var(--darker);display:flex;align-items:center;justify-content:center}

/* hero */
.hero{height:345px;background:radial-gradient(circle at 55% 50%,#e3262c,#a80c12 70%);position:relative;overflow:hidden}
.hero .copy{position:absolute;left:170px;top:80px;color:var(--white)}
.hero .kicker{font-family:Oswald,sans-serif;font-size:18px;color:#400;text-transform:uppercase;font-weight:500}
.hero h1{font-family:Oswald,sans-serif;font-size:30px;text-transform:uppercase;margin:2px 0 8px;font-weight:700}
.hero p{font-size:17px;line-height:22px;width:450px}
.hero-photo{position:absolute;left:700px;top:8px;width:280px;height:330px;background:linear-gradient(160deg,#d8d8d8,#2a2a2a 60%,#111);border-radius:18px}
.arrow{position:absolute;top:152px;width:40px;height:40px;border-radius:50%;border:2px solid var(--white);display:flex;align-items:center;justify-content:center}
.arrow.l{left:44px}.arrow.r{right:46px}

/* features band */
.features{height:129px;background:var(--dark);border-bottom:4px solid var(--red)}
.features .wrap{display:flex;padding-top:22px}
.feature{width:287px;color:#eee;font-size:14px;line-height:18px}
.feature h3{display:flex;align-items:center;gap:10px;font-size:22px;font-weight:400;margin-bottom:6px}
.feature svg{width:28px;height:28px}

/* main */
.main{display:flex;gap:24px;margin-top:36px}
.sidebar{width:236px}
.side-head{height:34px;background:linear-gradient(var(--red),var(--red-dark));color:var(--white);font-size:15px;font-weight:600;padding:7px 12px;border-radius:3px 3px 0 0}
.side-list{background:var(--panel);padding:4px 0 8px;margin-bottom:20px}
.side-list li{height:27px;line-height:27px;margin:0 6px;border-bottom:1px solid #d4d4d4;font-size:11px;font-weight:700;padding-left:14px;position:relative}
.side-list li::before{content:"";position:absolute;left:4px;top:10px;border:4px solid transparent;border-left-color:var(--red)}
.offer{border:1px solid var(--line);padding:8px 10px;margin-bottom:24px}
.offer p{font-size:11px;line-height:16px;margin-bottom:14px}
.cards{display:grid;grid-template-columns:1fr 1fr;gap:14px 18px;padding:0 6px}
.card{height:36px;border-radius:3px}
.promo-call{height:118px;background:linear-gradient(var(--red),var(--red-dark));border:3px solid #ddd;color:var(--white);text-align:center;font-family:Oswald,sans-serif;padding-top:14px;margin-bottom:10px}
.promo-call .a{font-size:24px}.promo-call .b{font-size:38px;line-height:44px}
.promo-deliver{height:143px;border:3px solid #ddd;background:linear-gradient(#5ca32c,#3a7a19 40%,#fff 40%);position:relative}
.promo-deliver .t{color:var(--white);font-family:Oswald,sans-serif;font-size:24px;padding:10px 12px}
.promo-deliver .van{position:absolute;left:12px;top:68px;width:100px;height:58px;background:#e9e14a;border-radius:4px}
.promo-deliver .tag{position:absolute;right:10px;top:74px;width:100px;height:38px;background:#f2d200;font-size:12px;font-weight:700;display:flex;align-items:center;justify-content:center}

.content{width:600px}
.sec-head{height:32px;background:var(--panel);border-left:4px solid #555;display:flex;align-items:center;padding:0 10px;font-size:15px;font-weight:600;justify-content:space-between;text-transform:uppercase}
.sec-head em{font-style:normal;color:var(--red)}
.viewall{background:#666;color:var(--white);font-size:10px;padding:3px 8px}
.intro{font-size:11px;line-height:17px;color:#444;padding:12px 0}
.bullets li{font-size:11px;line-height:17px;color:#444;padding-left:14px;position:relative}
.bullets li::before{content:"›";color:var(--red);position:absolute;left:2px;font-weight:700}
.products{display:grid;grid-template-columns:repeat(3,185px);gap:14px 22px;margin-top:20px}
.product{height:329px;border:1px solid var(--line);padding:8px}
.product .img{height:110px;background:radial-gradient(circle,#555 20%,#eee 50%);margin-bottom:12px}
.product .img.light{background:radial-gradient(circle,#bbb 20%,#eee 50%)}
.product .img.redish{background:radial-gradient(circle,#c33 20%,#eee 50%)}
.product .img.olive{background:radial-gradient(circle,#6f6a4a 20%,#eee 50%)}
.product h4{color:var(--red);font-size:13px;font-weight:600;margin-bottom:6px}
.product p{font-size:11px;line-height:15px;color:#444}
.product .size{margin:12px 0 6px}
.price{font-size:12px;white-space:nowrap}.price b{color:var(--red);font-size:22px;font-weight:700}
.btn{display:block;width:96px;margin:6px auto 0;height:20px;font-size:10px;font-weight:700;color:var(--white);text-align:center;line-height:20px;border-radius:2px}
.btn.add{background:var(--red)}.btn.det{background:#666}
.free{margin-top:26px;height:48px;background:linear-gradient(#3c6fe0,var(--blue));border-radius:6px;color:var(--white);font-family:Oswald,sans-serif;font-size:24px;text-align:center;line-height:48px;box-shadow:0 6px 8px rgba(0,0,0,.25)}

/* footer */
.footer{position:absolute;left:0;top:2144px;width:1200px;height:308px;background:var(--dark);border-top:4px solid var(--red);color:#ddd}
.footer .cols{display:flex;padding-top:30px}
.fcol{width:210px}.fcol:nth-child(3){width:242px}
.fcol h5{font-size:15px;font-weight:600;text-transform:uppercase;padding-bottom:6px;border-bottom:2px solid #ddd;width:165px;margin-bottom:10px}
.fcol li{font-size:11px;line-height:23px}
.fp{display:flex;gap:10px;margin-bottom:12px;font-size:11px}
.fp i{width:52px;height:52px;background:radial-gradient(circle,#c22 25%,#eee 55%);display:block;flex:none}
.fp i.k{background:radial-gradient(circle,#333 25%,#eee 55%)}
.fp b{display:block;color:var(--red);font-size:14px}
.copy-line{position:absolute;bottom:10px;width:100%;text-align:center;font-size:10px;color:#888}
</style>
</head>
<body>
<div class="topbar"><div class="wrap">
  <span>MY ACCOUNT</span><span class="sep">|</span><span>CHECKOUT</span><span class="sep">|</span><span>CART</span><span class="sep">|</span><span>LOGIN</span><span class="sep">|</span><span class="reg">REGISTER</span>
  <span class="social"><span></span><span></span><span></span><span></span></span>
</div></div>

<header class="header"><div class="wrap">
  <div class="logo"><i></i>Gearcrate</div>
  <div class="phone"><svg viewBox="0 0 24 24"><circle cx="12" cy="12" r="11" fill="#c8141c"/><path d="M8 6l2 3-1.5 1.5a8 8 0 004 4L14 13l3 2-1 2c-5 0-9-4-9-9z" fill="#fff"/></svg>01632 960400</div>
  <div class="cart"><b>YOUR CART</b>ITEMS (0)<br>$ 00.00
    <svg viewBox="0 0 46 40"><path d="M2 14h42l-5 22H7z" fill="none" stroke="#333" stroke-width="3"/><path d="M14 14l8-12M32 14l-8-12" stroke="#333" stroke-width="3"/></svg></div>
</div></header>

<nav class="nav"><div class="wrap">
  <span>HOME</span><span>MY ACCOUNT</span><span>CONTACT US</span><span>CHECKOUT</span><span>QUICK SEARCH</span>
  <div class="search">Search the product...<span><svg width="14" height="14" viewBox="0 0 14 14"><circle cx="6" cy="6" r="4" fill="none" stroke="#fff" stroke-width="2"/><path d="M9 9l4 4" stroke="#fff" stroke-width="2"/></svg></span></div>
</div></nav>

<section class="hero">
  <div class="copy">
    <div class="kicker">Consectetuer adipiscing elit, sed diam</div>
    <h1>Nostrud exerci tation ullamcorper</h1>
    <p>Lorem ipsum dolor sit amet, consectetuer adipiscing elit, sed diam nonummy nibh euismod tincidunt ut laoreet dolore magna aliquam erat volutpat.</p>
  </div>
  <div class="hero-photo" role="img" aria-label="Black and grey camera shoulder bag"></div>
  <div class="arrow l"><svg width="16" height="16" viewBox="0 0 16 16"><path d="M10 3L5 8l5 5" fill="none" stroke="#fff" stroke-width="2.5"/></svg></div>
  <div class="arrow r"><svg width="16" height="16" viewBox="0 0 16 16"><path d="M6 3l5 5-5 5" fill="none" stroke="#fff" stroke-width="2.5"/></svg></div>
</section>

<section class="features"><div class="wrap">
  <div class="feature"><h3><svg viewBox="0 0 28 28"><circle cx="14" cy="14" r="12" fill="none" stroke="#e0262c" stroke-width="3"/><path d="M14 7v8h6" stroke="#e0262c" stroke-width="3" fill="none"/></svg>24/7/365</h3>Great support anytime and anywhere<br>for our customers.</div>
  <div class="feature"><h3><svg viewBox="0 0 28 28"><path d="M6 3l5 6-3 3a14 14 0 008 8l3-3 6 5-3 4C12 26 2 16 2 6z" fill="#e0262c"/></svg>CALL US FREE</h3>Call us anytime for any kind of help,<br>we will be on spot.</div>
  <div class="feature"><h3><svg viewBox="0 0 28 28"><path d="M2 8h16v12H2zM18 12h5l4 4v4h-9z" fill="#e0262c"/><circle cx="7" cy="22" r="3" fill="#fff"/><circle cx="22" cy="22" r="3" fill="#fff"/></svg>FAST DELIVERY</h3>Order product until 00:00am / pm and<br>get it same day.</div>
</div></section>

<div class="wrap main">
  <aside class="sidebar">
    <div class="side-head">BROADCAST</div>
    <ul class="side-list">
      <li>Stowmate</li><li>Carrywell</li><li>Kestrow - Drift Cases.</li><li>Kestrow</li><li>Oreva</li><li>Brisko</li><li>JN Cases</li><li>Kitbay</li><li>Tuckbag</li>
    </ul>
    <div class="side-head">PHOTOGRAPHY</div>
    <ul class="side-list">
      <li>Kestrow - Drift Cases.</li><li>Rampart Hard Cases</li><li>Kestrow</li><li>Oreva</li><li>Hobnail</li><li>Fernleigh Bags</li><li>Hillmoor</li><li>Ostrel</li>
    </ul>
    <div class="side-head">WE OFFER</div>
    <div class="offer">
      <p>Lorem ipsum dolor sit amet, consectetuer adipiscing elit, sed diam nonummy nibh.</p>
      <div class="cards">
        <div class="card" style="background:#3a7bd5"></div><div class="card" style="background:#1a3d8f"></div>
        <div class="card" style="background:#e8a020"></div><div class="card" style="background:#1a3d8f"></div>
        <div class="card" style="background:#1a3d8f"></div><div class="card" style="background:#d33"></div>
        <div class="card" style="background:#2a6ad6"></div><div class="card" style="background:#b32"></div>
        <div class="card" style="background:#7a2a8a"></div><div class="card" style="background:#2a8ad6"></div>
      </div>
    </div>
    <div class="promo-call"><div class="a">ORDER ONLINE OR CALL:</div><div class="b">01632 960400</div></div>
    <div class="promo-deliver">
      <div class="t">DELIVERY INCLUDED</div>
      <div class="van" role="img" aria-label="Delivery van"></div>
      <div class="tag">IN ALL PRICES*</div>
    </div>
  </aside>

  <main class="content">
    <div class="sec-head"><span>Welcome to <em>Gearcrate</em></span></div>
    <p class="intro">Gearcrate are a leading distributor to the film, television and photographic industries. We stock thousands of quality products from Kestrow, Hobnail, Fernleigh, Oreva, Quent, Duvo, Ostrel, Brisko, Carrywell, Hillmoor, Tavrin and other leading manufacturers. These products include:</p>
    <ul class="bullets">
      <li>Kestrow camera cases, Kestrow director cases, Kestrow projector cases and Kestrow audio cases</li>
      <li>Hobnail camera cases, Hobnail laptop bags and Hobnail bags</li>
      <li>Fernleigh camera bags, Fernleigh pockets and Fernleigh stowaway bags</li>
      <li>Oreva mixer cases, Oreva organiser bags, Oreva body armour and accessories</li>
      <li>Ostrel camera bags and Ostrel backpacks</li>
      <li>Brisko camera bags, Brisko camera covers and Brisko lighting bags</li>
      <li>Carrywell audio cases, Carrywell camera cases and Carrywell computer cases</li>
    </ul>
    <div class="sec-head" style="margin-top:18px"><span>Featured <em>Products</em></span><span class="viewall">VIEW ALL</span></div>
    <div class="products">
      <div class="product"><div class="img" role="img" aria-label="Black camera pouch"></div><h4>Hobnail Nudge 500</h4><p>Model Hobnail Nudge 500 Fits SLR with long tele lens</p><p class="size">Size inside: 17.0 x 23.0 x 11.0 cm</p><div class="price">Price: (exc VAT) <b>£30.86</b></div><span class="btn add">ADD TO CART</span><span class="btn det">DETAILS</span></div>
      <div class="product"><div class="img light" role="img" aria-label="White camera pouch"></div><h4>Hobnail Nudge 600</h4><p>Model Hobnail Nudge 600 Fits SLR with long tele lens</p><p class="size">Size inside: 17.0 x 23.0 x 11.0 cm</p><div class="price">Price: (exc VAT) <b>£30.86</b></div><span class="btn add">ADD TO CART</span><span class="btn det">DETAILS</span></div>
      <div class="product"><div class="img" role="img" aria-label="Black camera pouch"></div><h4>Hobnail Nudge 700</h4><p>Model Hobnail Nudge 700 Fits SLR with long tele lens</p><p class="size">Size inside: 17.0 x 23.0 x 11.0 cm</p><div class="price">Price: (exc VAT) <b>£30.86</b></div><span class="btn add">ADD TO CART</span><span class="btn det">DETAILS</span></div>
      <div class="product"><div class="img" role="img" aria-label="Dark camera bag"></div><h4>Hobnail Crumb Top 55</h4><p>Model Hobnail Nudge 500 Fits SLR with long tele lens</p><p class="size">Size inside: 17.0 x 23.0 x 11.0 cm</p><div class="price">Price: (exc VAT) <b>£30.86</b></div><span class="btn add">ADD TO CART</span><span class="btn det">DETAILS</span></div>
      <div class="product"><div class="img redish" role="img" aria-label="Red camera bag"></div><h4>Hobnail Crumb Top 80</h4><p>Model Hobnail Nudge 500 Fits SLR with long tele lens</p><p class="size">Size inside: 17.0 x 23.0 x 11.0 cm</p><div class="price">Price: (exc VAT) <b>£30.86</b></div><span class="btn add">ADD TO CART</span><span class="btn det">DETAILS</span></div>
      <div class="product"><div class="img olive" role="img" aria-label="Olive camera bag"></div><h4>Hobnail Nudge 500</h4><p>Model Hobnail Nudge 500 Fits SLR with long tele lens</p><p class="size">Size inside: 17.0 x 23.0 x 11.0 cm</p><div class="price">Price: (exc VAT) <b>£30.86</b></div><span class="btn add">ADD TO CART</span><span class="btn det">DETAILS</span></div>
      <div class="product"><div class="img" role="img" aria-label="Black camera pouch"></div><h4>Hobnail Nudge 500</h4><p>Model Hobnail Nudge 500 Fits SLR with long tele lens</p><p class="size">Size inside: 17.0 x 23.0 x 11.0 cm</p><div class="price">Price: (exc VAT) <b>£30.86</b></div><span class="btn add">ADD TO CART</span><span class="btn det">DETAILS</span></div>
      <div class="product"><div class="img light" role="img" aria-label="White camera pouch"></div><h4>Hobnail Nudge 600</h4><p>Model Hobnail Nudge 600 Fits SLR with long tele lens</p><p class="size">Size inside: 17.0 x 23.0 x 11.0 cm</p><div class="price">Price: (exc VAT) <b>£30.86</b></div><span class="btn add">ADD TO CART</span><span class="btn det">DETAILS</span></div>
    </div>
    <div class="free">FREE CAMERA CASE WITH ALL ORDERS*</div>
  </main>
</div>

<footer class="footer">
  <div class="wrap cols">
    <div class="fcol"><h5>Quick Links</h5><ul><li>Home</li><li>My Account</li><li>Contact us</li><li>Checkout</li></ul></div>
    <div class="fcol"><h5>Information</h5><ul><li>About Us</li><li>Kestrow Case FAQ's</li><li>Kestrow Size Guide</li><li>Privacy Policy</li><li>Shipping and Returns</li><li>Drift Case FAQ's</li><li>Terms &amp; Conditions</li></ul></div>
    <div class="fcol"><h5>Important Links</h5><ul><li>Carrywell cases</li><li>Kestrow products</li><li>Oreva products</li><li>Tavrin products</li><li>Kestrow cases for the broadcast industry</li><li>Kestrow cases for the photography industry</li></ul></div>
    <div class="fcol"><h5>Featured Products</h5>
      <div class="fp"><i role="img" aria-label="Red camera bag"></i><span>consectetuer adipiscing<b>£30.86</b></span></div>
      <div class="fp"><i class="k" role="img" aria-label="Black camera pouch"></i><span>Quis nostrud exerci tation<br>ullamcorper<b>£30.86</b></span></div>
    </div>
  </div>
  <div class="copy-line">© Copyright 2007 Gearcrate. All Right Reserved</div>
</footer>
</body>
</html>
```